Poster Design Project- New Years Eve

We are a fun and quirky bar in St Kilda (www.quillhouse.com.au). We need a poster designed for our New Years Eve Event- details as follows
Project: A1 poster-NYE
Name of Event: Copper Moons
Date of Event: New Years Eve: 31.12.12
Tagline: ‘What happens at Quill stays at Quill’
Time: 8pm-3am
Cost:
$105 all inclusive
-Includes a cocktail on arrival
-4 hour drink package – Basic Spirits, Premium Beer, Wine and Sparkling til 12AM
-Grazing style canapés and finger food
Early bird and group discounts (10+) available
Purchase your tickets at the bar or through the website
Dress: For Fun and Dancing
Venue information:
• Address: 47 Brambleton Lane St Kilda
• Phone: 6143 2057
• Email: info@quillhouse.com.au
• Website: www.quillhouse.com.au
• Management reserves the right to refuse entry
Images: Images need to be high resolution or vector images so clarity is not lost when the poster is blown up to this size
Poster production:
Poster needs to be created in either Adobe Illustrator or Photoshop so we can easily edit the details if they change after the contest ends
Please provide 3mm internal and external bleed
Theming:
Fun poster with elements of Las Vegas including: dice/casino element, Las Copper Moons, pretty girls, cocktails
25-40 year olds
Casino

```html
<!DOCTYPE html>
<html lang="en">
<head>
<meta charset="utf-8">
<title>Copper Moons – New Years Eve at Quill</title>
<link rel="stylesheet" href="https://fonts.googleapis.com/css2?family=Passion+One:wght@700&family=Francois+One&family=Arimo:wght@400;700&display=swap">
<style>
  :root {
    --night: #050308;
    --ray: rgba(255, 255, 255, 0.16);
    --pink: #ff1e9c;
    --pink-deep: #c4006e;
    --yellow: #ffe600;
    --white: #ffffff;
    --photo-a: #6a5a73;
    --photo-b: #1d1624;
  }
  * { margin: 0; padding: 0; box-sizing: border-box; }
  html, body { width: 880px; height: 1200px; overflow: hidden; background: var(--night); }
  .poster {
    position: relative; width: 880px; height: 1200px; overflow: hidden;
    background: radial-gradient(ellipse at 50% 30%, #2a2230 0%, var(--night) 70%);
    font-family: "Francois One", "Arial Narrow", sans-serif; color: var(--yellow);
  }
  .spotlights { position: absolute; inset: 0; }
  .dancers-photo {
    position: absolute; left: 40px; top: 110px; width: 800px; height: 360px;
    background: radial-gradient(ellipse at 50% 45%, var(--photo-a) 0%, var(--photo-b) 60%, transparent 78%);
    opacity: .85;
  }
  .event-title { position: absolute; left: 0; top: 20px; width: 880px; height: 200px; }
  .event-title text {
    font-family: "Passion One", "Arial Black", sans-serif; font-size: 108px;
    fill: var(--pink); stroke: var(--yellow); stroke-width: 3px; paint-order: stroke; letter-spacing: 4px;
  }
  .centre { position: absolute; left: 0; width: 880px; text-align: center; }
  .occasion { top: 276px; font-size: 36px; }
  .date { top: 312px; font-size: 74px; color: var(--pink); -webkit-text-stroke: 1px var(--yellow); letter-spacing: 2px; }
  .tagline { top: 395px; font-size: 42px; }
  .time-label { top: 448px; font-size: 38px; color: var(--pink); }
  .time { top: 482px; font-size: 52px; }
  .cost { top: 540px; font-size: 40px; }
  .notes { top: 596px; font-family: "Arimo", Arial, sans-serif; font-size: 21px; color: var(--white); line-height: 1.2; }
  .venue-mark {
    position: absolute; top: 440px; display: flex; align-items: center; gap: 10px;
    font-size: 34px; color: var(--white);
  }
  .venue-mark .dot { width: 16px; height: 16px; border-radius: 50%; background: var(--pink); }
  .venue-mark.left { left: 60px; }
  .venue-mark.right { right: 50px; }
  .details { position: absolute; top: 670px; left: 0; width: 880px; display: flex; }
  .dress { width: 430px; padding-left: 22px; }
  .dress h2, .venue h2 { font-weight: 400; font-size: 38px; color: var(--yellow); margin-bottom: 14px; }
  .inclusions { list-style: none; font-family: "Arimo", Arial, sans-serif; font-size: 20px; color: var(--white); }
  .inclusions li { position: relative; padding-left: 28px; margin-bottom: 12px; line-height: 1.25; }
  .inclusions li::before { content: "★"; position: absolute; left: 0; color: var(--yellow); }
  .venue { width: 450px; padding-left: 10px; }
  .venue dl { font-family: "Arimo", Arial, sans-serif; font-size: 20px; font-weight: 700; line-height: 1.5; }
  .venue .row { display: flex; gap: 6px; }
  .venue dt { color: var(--pink); }
  .venue dd { color: var(--white); }
  .venue .rule { color: var(--pink); }
</style>
</head>
<body>
<main class="poster">
  <svg class="spotlights" width="880" height="1200" viewBox="0 0 880 1200" aria-hidden="true">
    <g fill="var(--ray)">
      <polygon points="440,0 380,0 120,520 260,520"/>
      <polygon points="440,0 500,0 760,520 620,520"/>
      <polygon points="440,0 420,0 360,600 520,600"/>
      <polygon points="0,0 60,0 300,460 200,460"/>
      <polygon points="880,0 820,0 580,460 680,460"/>
    </g>
  </svg>

  <div class="dancers-photo" role="img" aria-label="Photo of three young women dancing under stage lights"></div>

  <svg class="event-title" viewBox="0 0 880 200" aria-label="Copper Moons">
    <path id="title-arc" d="M40,190 Q440,20 840,190" fill="none"/>
    <text text-anchor="middle"><textPath href="#title-arc" startOffset="50%">COPPER MOONS</textPath></text>
  </svg>

  <p class="centre occasion">NEW YEARS EVE</p>
  <p class="centre date">31.12.12</p>
  <p class="centre tagline">What happens at Quill stays at Quill</p>

  <div class="venue-mark left"><span class="dot"></span>Quill House</div>
  <div class="venue-mark right"><span class="dot"></span>Quill House</div>

  <p class="centre time-label">Time</p>
  <p class="centre time">8PM-3AM</p>
  <p class="centre cost">COST: $ 105 all inclusive</p>
  <p class="centre notes">Early bird and group discounts (10+) available<br>Purchase your tickets at the bar or through the website</p>

  <section class="details">
    <div class="dress">
      <h2>Dress: For Fun and Dancing</h2>
      <ul class="inclusions">
        <li>Includes a cocktail on arrival</li>
        <li>4 hour drink package - Basic Spirits, Premium Beer, Wine and Sparkling til 12AM</li>
        <li>Grazing style canapés and finger food</li>
      </ul>
    </div>
    <div class="venue">
      <h2>VENUE INFORMATION</h2>
      <dl>
        <div class="row"><dt>Address:</dt><dd>47 Brambleton Lane St Kilda</dd></div>
        <div class="row"><dt>Phone:</dt><dd>6143 2057</dd></div>
        <div class="row"><dt>Email:</dt><dd>info@quillhouse.com.au</dd></div>
        <div class="row"><dt>Website:</dt><dd>www.quillhouse.com.au</dd></div>
      </dl>
      <p class="venue rule" style="font-family:'Arimo',Arial,sans-serif;font-size:20px;font-weight:700;padding:0;width:auto;">Management reserves the right to refuse entry</p>
    </div>
  </section>
</main>
</body>
</html>
```